Business Card Design Project

We're an orthopaedic office, and our colors are blue white and balck. Dealing with physicians and healthcare execs, I'd like this card to have a classy, yet overpowering wow factor.

Here are a couple of cards I like that are close to what I'm looking for:
http://www.plumvantia.com/design/671583
http://www.plumvantia.com/design/514515

```html
<!DOCTYPE html>
<html lang="en">
<head>
<meta charset="utf-8">
<title>Harlow Ridge Orthopaedic &amp; Sports Medicine Center – Business Card</title>
<link rel="stylesheet" href="https://fonts.googleapis.com/css2?family=Questrial&display=swap">
<style>
  :root {
    --brand-blue: #2d33a6;
    --card-white: #f7f7f9;
    --watermark-light: #e6e7ef;
    --watermark-blue: #3a41b4;
    --stage: #d9dade;
    --ink-blue: #2d33a6;
  }
  * { box-sizing: border-box; margin: 0; padding: 0; }
  html, body { width: 1200px; height: 900px; overflow: hidden; }
  body {
    background: var(--stage);
    font-family: "Questrial", "Century Gothic", sans-serif;
    position: relative;
  }
  .card {
    position: absolute;
    width: 560px;
    height: 320px;
    overflow: hidden;
    box-shadow: 0 10px 24px rgba(0,0,0,0.25);
  }
  .card--front { left: 60px; top: 110px; background: var(--card-white); color: var(--ink-blue); }
  .card--back  { left: 580px; top: 470px; background: var(--brand-blue); color: #fff; }

  .watermark { position: absolute; border-radius: 50%; }
  .card--front .watermark {
    width: 300px; height: 300px; right: -40px; top: -70px;
    border: 38px solid var(--watermark-light);
  }
  .card--back .watermark {
    width: 320px; height: 320px; right: -60px; top: -60px;
    border: 40px solid var(--watermark-blue);
  }

  .brand { display: flex; align-items: center; gap: 14px; }
  .brand__dot { border-radius: 50%; flex: none; }
  .brand__name { text-transform: uppercase; line-height: 1; }
  .brand__sub { text-transform: uppercase; line-height: 1.15; }
  .brand__tag { line-height: 1.2; }

  .card--front .brand { position: absolute; left: 36px; top: 40px; }
  .card--front .brand__dot { width: 54px; height: 54px; background: var(--brand-blue); }
  .card--front .brand__name { font-size: 30px; letter-spacing: 0.5px; }
  .card--front .brand__sub { font-size: 13px; letter-spacing: 0.3px; margin-top: 2px; }
  .card--front .brand__tag { font-size: 11px; text-align: right; }

  .person { position: absolute; left: 36px; top: 138px; }
  .person__name { font-size: 19px; letter-spacing: 1.5px; text-transform: uppercase; }
  .person__title { font-size: 13px; margin-top: 2px; }

  .contact { position: absolute; left: 36px; top: 200px; list-style: none; }
  .contact__item { display: flex; align-items: center; gap: 8px; font-size: 14px; margin-bottom: 6px; }
  .contact__icon { width: 14px; height: 14px; flex: none; }

  .card--back .brand {
    position: absolute; left: 0; right: 0; top: 42px;
    flex-direction: column; gap: 14px; text-align: center;
  }
  .card--back .brand__dot { width: 70px; height: 70px; background: #fff; }
  .card--back .brand__name { font-size: 48px; letter-spacing: 1px; }
  .card--back .brand__sub { font-size: 21px; letter-spacing: 0.5px; margin-top: 6px; }
  .card--back .brand__tag { font-size: 17px; margin-top: 2px; }
</style>
</head>
<body>

  <section class="card card--front" aria-label="Business card front">
    <div class="watermark" aria-hidden="true"></div>

    <div class="brand">
      <span class="brand__dot" aria-hidden="true"></span>
      <div>
        <div class="brand__name">Harlow Ridge</div>
        <div class="brand__sub">Orthopaedic &amp; Sports</div>
        <div class="brand__tag">Medicine Center</div>
      </div>
    </div>

    <div class="person">
      <div class="person__name">Dalton Reeve</div>
      <div class="person__title">CEO</div>
    </div>

    <ul class="contact">
      <li class="contact__item">
        <svg class="contact__icon" viewBox="0 0 14 14"><rect x="0.5" y="0.5" width="13" height="13" rx="2" fill="none" stroke="currentColor"/><path d="M4 3.5h2l.6 2-1.2.8a6 6 0 0 0 2.3 2.3l.8-1.2 2 .6v2c-4 .3-6.8-2.5-6.5-6.5z" fill="currentColor"/></svg>
        (318) 555-0142
      </li>
      <li class="contact__item">
        <svg class="contact__icon" viewBox="0 0 14 14"><rect x="0.5" y="0.5" width="13" height="13" rx="2" fill="none" stroke="currentColor"/><rect x="3" y="4.5" width="8" height="5.5" fill="none" stroke="currentColor"/><path d="M3 4.5l4 3 4-3" fill="none" stroke="currentColor"/></svg>
        dreeve@harlowridgeortho.com
      </li>
      <li class="contact__item">
        <svg class="contact__icon" viewBox="0 0 14 14"><rect x="0.5" y="0.5" width="13" height="13" rx="2" fill="none" stroke="currentColor"/><circle cx="7" cy="7" r="3.5" fill="none" stroke="currentColor"/><path d="M3.5 7h7M7 3.5c-1.5 2-1.5 5 0 7M7 3.5c1.5 2 1.5 5 0 7" fill="none" stroke="currentColor" stroke-width="0.8"/></svg>
        www.harlowridgeortho.com
      </li>
      <li class="contact__item">
        <svg class="contact__icon" viewBox="0 0 14 14"><rect x="0.5" y="0.5" width="13" height="13" rx="2" fill="none" stroke="currentColor"/><path d="M7 11.5s-3-3-3-5.3a3 3 0 0 1 6 0c0 2.3-3 5.3-3 5.3z" fill="currentColor"/><circle cx="7" cy="6.2" r="1" fill="#fff"/></svg>
        1870 Cedar Bend Dr. Pinehaven, LA 70999
      </li>
    </ul>
  </section>

  <section class="card card--back" aria-label="Business card back">
    <div class="watermark" aria-hidden="true"></div>
    <div class="brand">
      <span class="brand__dot" aria-hidden="true"></span>
      <div>
        <div class="brand__name">Harlow Ridge</div>
        <div class="brand__sub">Orthopaedic &amp; Sports</div>
        <div class="brand__tag">Medicine Center</div>
      </div>
    </div>
  </section>

</body>
</html>
```